North Fern Holdings Business Card

A business card design to accompany the logo design you completed on Artisan Hive. We are open to your proposals. I did add one idea below that might work, but we aren't married to the idea. The company is a real estate services company. Clientele are typically high net worth individuals, executive level employment or owners of their own company, 30-60 years old.

Our 1 (bad?) idea: double sided card; One side landscape with logo and word mark. Other side Portrait with the logo only (oversize watermark maybe?). Somewhere add text of Name (Marcus Pellington), Title (Principal), phone # (949-555-0173) and email address (marcus@northfernhq.com). There would be a second design with my wife's name, number and email in place of mine.

Again totally open to ideas here.

Industry/Entity Type

Real Estate

```html
<!DOCTYPE html>
<html lang="en">
<head>
<meta charset="utf-8">
<title>North Fern Holdings — Business Card</title>
<link href="https://fonts.googleapis.com/css2?family=Open+Sans:wght@400;600;700&display=swap" rel="stylesheet">
<style>
  :root {
    --sage: #5f9459;
    --sage-light: #6ea267;
    --slate: #76787b;
    --paper: #ffffff;
    --backdrop: #ecebe7;
    --ink-light: #ffffff;
  }
  * { box-sizing: border-box; margin: 0; padding: 0; }
  html, body {
    width: 1200px; height: 1014px; overflow: hidden;
    background: var(--backdrop);
    font-family: "Open Sans", Arial, sans-serif;
  }
  .canvas { position: relative; width: 1200px; height: 1014px; }

  .card {
    position: absolute;
    box-shadow: 0 6px 18px rgba(0,0,0,0.18);
    overflow: hidden;
  }

  /* Front (landscape) */
  .card-front {
    left: 50px; top: 150px;
    width: 620px; height: 354px;
    background: var(--paper);
  }
  .card-front .swoosh { position: absolute; inset: 0; }
  .brand {
    position: absolute;
    left: 34px; top: 104px;
    display: flex; align-items: center; gap: 12px;
  }
  .brand-square {
    width: 26px; height: 26px;
    background: var(--sage);
    flex: none;
  }
  .brand-name {
    font-weight: 600;
    font-size: 20px;
    letter-spacing: 1px;
    color: var(--sage);
    text-transform: uppercase;
    white-space: nowrap;
  }
  .person {
    position: absolute;
    left: 330px; bottom: 30px;
    color: var(--ink-light);
    white-space: nowrap;
  }
  .person-name { font-weight: 700; font-size: 21px; line-height: 1.2; }
  .person-title { font-weight: 400; font-size: 17px; line-height: 1.3; }
  .contact {
    position: absolute;
    right: 24px; top: 112px;
    color: var(--ink-light);
    font-size: 13px; line-height: 1.55;
    list-style: none;
    text-align: right;
    white-space: nowrap;
  }

  /* Back (portrait) */
  .card-back {
    left: 760px; top: 150px;
    width: 354px; height: 620px;
    background: linear-gradient(135deg, var(--sage) 0%, var(--sage-light) 50%, var(--sage) 100%);
    display: flex; align-items: center; justify-content: center;
  }
  .back-mark {
    color: var(--ink-light);
    font-weight: 600;
    font-size: 24px;
    letter-spacing: 1.5px;
    text-transform: uppercase;
    text-align: center;
    line-height: 1.3;
  }
</style>
</head>
<body>
<main class="canvas">
  <section class="card card-front" aria-label="Business card front">
    <svg class="swoosh" width="620" height="354" viewBox="0 0 620 354" aria-hidden="true">
      <path d="M440,0 C415,160 340,290 210,354 L620,354 L620,0 Z" fill="var(--sage)"/>
      <path d="M462,0 C439,160 366,292 238,354 L620,354 L620,0 Z" fill="var(--slate)" stroke="var(--paper)" stroke-width="4"/>
    </svg>

    <div class="brand">
      <span class="brand-square" aria-hidden="true"></span>
      <span class="brand-name">North Fern Holdings</span>
    </div>

    <div class="person">
      <p class="person-name">Marcus Pellington</p>
      <p class="person-title">Principal</p>
    </div>

    <ul class="contact">
      <li>phone 949.555.0173</li>
      <li>marcus@northfernhq.com</li>
      <li>www.northfernhq.com</li>
    </ul>
  </section>

  <section class="card card-back" aria-label="Business card back">
    <p class="back-mark">North Fern<br>Holdings</p>
  </section>
</main>
</body>
</html>
```